New bussiness card, using company logo.
Lachlan Voss
Manager/Director
Birch Property Developments
Po Box 4657
Wrenvale Central
Nrd
0455 386 218
lachlan@birchpropertydevelopments
eye catching, vibrant colours, professional

```html
<!DOCTYPE html>
<html lang="en">
<head>
<meta charset="utf-8">
<title>Birch Property Developments – Business Card</title>
<link rel="stylesheet" href="https://fonts.googleapis.com/css2?family=PT+Sans:wght@400;700&display=swap">
<style>
  :root {
    --backdrop: #5f7479;
    --card-white: #ffffff;
    --card-grey: #6e6e6e;
    --brand-red: #d8232a;
    --brand-green: #7dc242;
    --text-light: #ffffff;
    --shadow: rgba(0, 0, 0, 0.35);
  }
  * { box-sizing: border-box; margin: 0; padding: 0; }
  html, body {
    width: 1200px;
    height: 960px;
    overflow: hidden;
  }
  body {
    background: var(--backdrop);
    font-family: "PT Sans", sans-serif;
    display: flex;
    flex-direction: column;
    align-items: center;
    justify-content: center;
    gap: 40px;
  }
  .card {
    width: 735px;
    height: 420px;
    background: var(--card-white);
    box-shadow: 0 10px 30px var(--shadow);
    position: relative;
    overflow: hidden;
  }

  /* Brand lockup: name in one colour and weight, with a single square */
  .brand {
    display: flex;
    align-items: center;
    gap: 14px;
    color: var(--brand-red);
    font-weight: 700;
    white-space: nowrap;
  }
  .brand__mark {
    width: 26px;
    height: 26px;
    background: var(--brand-green);
    flex: none;
  }

  /* Front card with details */
  .card--front .card__top {
    height: 196px;
    display: flex;
    align-items: center;
    justify-content: center;
  }
  .card--front .brand { font-size: 34px; }
  .card__divider {
    height: 8px;
    background: var(--brand-red);
  }
  .card__details {
    height: calc(420px - 196px - 8px);
    background: var(--card-grey);
    color: var(--text-light);
    display: flex;
    padding: 24px 0 0 0;
  }
  .person {
    width: 330px;
    padding: 26px 0 0 70px;
  }
  .person__name {
    font-size: 30px;
    font-weight: 400;
    line-height: 1.15;
  }
  .person__role {
    font-size: 22px;
    margin-left: 14px;
    line-height: 1.3;
  }
  .contact {
    font-style: normal;
    font-size: 17px;
    line-height: 1.4;
  }

  /* Back card with logo only */
  .card--back {
    display: flex;
    align-items: center;
    justify-content: center;
  }
  .card--back .brand { font-size: 44px; }
</style>
</head>
<body>

  <section class="card card--front" aria-label="Business card front">
    <div class="card__top">
      <div class="brand">
        <span class="brand__mark" aria-hidden="true"></span>
        <span class="brand__name">Birch Property Developments</span>
      </div>
    </div>
    <div class="card__divider"></div>
    <div class="card__details">
      <div class="person">
        <p class="person__name">Lachlan Voss</p>
        <p class="person__role">Manager/Director</p>
      </div>
      <address class="contact">
        Po Box 4657<br>
        Wrenvale Central<br>
        Nrd<br>
        0455 386 218<br>
        lachlan@birchpropertydevelopments
      </address>
    </div>
  </section>

  <section class="card card--back" aria-label="Business card back">
    <div class="brand">
      <span class="brand__mark" aria-hidden="true"></span>
      <span class="brand__name">Birch Property Developments</span>
    </div>
  </section>

</body>
</html>
```